Landing page for 'Page under construction' page

We need a simple landing page that we can use while our page is under construction.

The page should be made ready so that all we need to do is drop it on our web server and then it will function as our webpage. The domain is www.tlv.no

Please see attached file for instructions on what elements to include in the landing page. The Brand Book provides fonts and color palette.

Coding

Coded - Design and coding required

Number of Pages Required

1 page

Colors

Designer to choose colors to be used in the design.

```html
<!DOCTYPE html>
<html lang="en">
<head>
<meta charset="utf-8">
<title>TLV Consulting – Page under construction</title>
<link href="https://fonts.googleapis.com/css2?family=Montserrat:wght@400;500;600;700;800;900&family=Lato:wght@400&display=swap" rel="stylesheet">
<style>
  :root{
    --navy:#0a3568;
    --blue:#2b8fcc;
    --coral:#ec5a5a;
    --orange:#f59846;
    --ink:#111418;
    --mist:#eaf2fb;
    --white:#ffffff;
    --field-text:#8a8f96;
  }
  *{box-sizing:border-box;margin:0;padding:0}
  html,body{width:750px;height:1200px;overflow:hidden;background:var(--white)}
  body{font-family:"Montserrat",sans-serif;color:var(--ink);position:relative}

  .site-header{position:absolute;top:0;left:0;width:750px;height:70px;z-index:3}
  .brand{position:absolute;left:32px;top:22px;font-weight:800;font-size:20px;color:var(--navy);letter-spacing:-0.3px}
  .main-nav{position:absolute;left:0;top:0;width:750px;height:70px;font-size:10px;font-weight:500;color:var(--navy)}
  .main-nav a{position:absolute;top:30px;color:inherit;text-decoration:none;white-space:nowrap}
  .nav-epm{left:282px}
  .nav-lowcode{left:324px}
  .nav-customers{left:390px}
  .nav-resources{left:465px}
  .nav-about{left:524px}
  .nav-lang{left:577px}
  .btn-talk{position:absolute;left:631px;top:27px;width:84px;height:20px;border-radius:10px;background:linear-gradient(90deg,var(--coral),var(--orange));color:var(--white);font-size:7px;font-weight:700;letter-spacing:.4px;display:flex;align-items:center;justify-content:center;text-decoration:none}

  .hero{position:absolute;top:0;left:0;width:750px;height:440px;overflow:hidden}
  .hero-waves{position:absolute;inset:0;width:750px;height:440px}
  .hero-art{position:absolute;left:292px;top:128px;width:452px;height:238px;border-radius:6px;
    background:linear-gradient(135deg,rgba(245,152,70,.85) 0%,rgba(224,228,235,.9) 45%,rgba(79,182,212,.85) 100%)}
  .hero-copy{position:absolute;left:24px;top:150px;width:240px}
  .hero-title{font-weight:900;font-size:26px;line-height:1.05;color:var(--navy);letter-spacing:.2px}
  .title-rule{display:block;width:88px;height:3px;background:var(--coral);margin:5px 0 0 3px}
  .hero-text{font-size:7px;line-height:1.3;margin-top:18px}
  .hero-text p+p{margin-top:8px}

  .vision{position:absolute;top:455px;left:0;width:750px}
  .section-title{text-align:center;font-weight:700;font-size:22px;color:var(--navy)}
  .section-rule{display:block;width:60px;height:3px;background:var(--coral);margin:7px auto 0}
  .pillar{position:absolute;left:60px;width:640px}
  .pillar-icon{position:absolute;left:0;top:0}
  .pillar-title{position:absolute;left:47px;top:0;font-weight:600;font-size:11.5px;color:var(--blue)}
  .pillar-text{position:absolute;left:47px;top:18px;font-size:8.6px;line-height:1.28;color:var(--ink)}
  .pillar-vision{top:55px}
  .pillar-vision .pillar-text{left:52px;width:370px}
  .pillar-focus{top:110px}
  .pillar-focus .pillar-text{width:600px}

  .focus-diagram{position:absolute;left:161px;top:675px;width:436px;height:180px}

  .contact{position:absolute;top:872px;left:0;width:750px;height:282px;background:var(--mist)}
  .contact .section-title{margin-top:16px;font-size:23px}
  .contact-form{position:absolute;left:246px;top:80px;width:258px}
  .field{position:absolute;height:23px;background:var(--white);border:none;border-radius:2px;font-family:"Lato",sans-serif;font-size:6px;color:var(--field-text);padding:8px 9px}
  .f-first{left:0;top:0;width:123px}
  .f-last{left:135px;top:0;width:123px}
  .f-mail{left:0;top:38px;width:123px}
  .f-phone{left:135px;top:38px;width:123px}
  .f-message{left:0;top:75px;width:258px;height:66px}
  .btn-send{position:absolute;left:69px;top:170px;width:124px;height:30px;border-radius:15px;background:linear-gradient(90deg,var(--coral),var(--orange));color:var(--white);font-weight:700;font-size:10.5px;letter-spacing:.6px;display:flex;align-items:center;justify-content:center}
</style>
</head>
<body>

<section class="hero">
  <svg class="hero-waves" viewBox="0 0 750 497" preserveAspectRatio="none" aria-hidden="true">
    <path fill="#2b8fcc" d="M690 0 L750 0 L750 497 L158 497 C160 430 190 380 260 362 C330 344 420 332 452 262 C482 196 560 184 622 164 C688 142 682 60 690 0 Z"/>
    <path fill="#0a3568" d="M720 0 L750 0 L750 497 L196 497 C205 440 240 402 300 386 C380 366 452 342 482 282 C512 222 600 212 652 192 C722 164 712 80 720 0 Z"/>
  </svg>
  <div class="hero-art" role="img" aria-label="Illustration of construction workers with a megaphone, barriers, traffic cones and a ladder building a website on large screens"></div>
  <div class="hero-copy">
    <h1 class="hero-title">PAGE IS UNDER<br>CONSTRUCTION</h1>
    <span class="title-rule"></span>
    <div class="hero-text">
      <p>Digital solutions and data-driven business development that create value.</p>
      <p>TLV Consulting is a consulting company with cutting-edge expertise in digitalisation and data-driven business development. We have extensive experience in data warehouse development, data analysis and reporting, EPM and planning solutions, budget and forecasting solutions for financial and financial data. In short, we help our customers exploit the potential in the available data.</p>
    </div>
  </div>
</section>

<header class="site-header">
  <div class="brand">tallvik</div>
  <nav class="main-nav">
    <a class="nav-epm" href="#">EPM</a>
    <a class="nav-lowcode" href="#">Low-Code</a>
    <a class="nav-customers" href="#">Customers</a>
    <a class="nav-resources" href="#">Resources</a>
    <a class="nav-about" href="#">About</a>
    <a class="nav-lang" href="#">EN&#9662;</a>
  </nav>
  <a class="btn-talk" href="#contact">TALK TO US</a>
</header>

<section class="vision">
  <h2 class="section-title">TLV vision and TLV focus</h2>
  <span class="section-rule"></span>

  <div class="pillar pillar-vision">
    <svg class="pillar-icon" width="40" height="22" viewBox="0 0 40 22" aria-hidden="true">
      <path d="M1 11 C10 1 30 1 39 11 C30 21 10 21 1 11 Z" fill="#2b8fcc"/>
      <circle cx="20" cy="11" r="7.5" fill="#fff"/>
      <circle cx="20" cy="11" r="5" fill="none" stroke="#2b8fcc" stroke-width="2"/>
      <circle cx="20" cy="11" r="2" fill="#2b8fcc"/>
    </svg>
    <h3 class="pillar-title">TLV Vision</h3>
    <p class="pillar-text">TLV will be the country's leading supplier and competence house on Tallvik software and digital solutions for business management.</p>
  </div>

  <div class="pillar pillar-focus">
    <svg class="pillar-icon" width="34" height="30" viewBox="0 0 34 30" aria-hidden="true" style="left:6px;top:-4px">
      <circle cx="15" cy="15" r="10" fill="none" stroke="#2b8fcc" stroke-width="2"/>
      <circle cx="15" cy="15" r="5" fill="none" stroke="#2b8fcc" stroke-width="1.6"/>
      <path d="M15 1 V8 M15 22 V29 M1 15 H8 M22 15 H29" stroke="#2b8fcc" stroke-width="2"/>
    </svg>
    <h3 class="pillar-title">TLV Focus</h3>
    <p class="pillar-text">I TLV Focus er vi brennende opptatt av å utvikle gode løsninger som støtter opp om kundens digitale strategi. Vi har spesialisert oss på å levere konsulenttjenester og løsninger innenfor datavarehus, datavisualisering, integrasjoner og maskinlæring for store kunder over hele landet. Felles for disse er bruk av nyeste teknologi, hovedsakelig på Cloudvale plattformen, der vi som leverandør ivaretar flere roller som rådgivere, arkitekter og utviklere. Vi utvikler dataplattformer i Skyvault og har bred kompetanse på utvikling og implementering av Insight Studio. Vi utvikler integrasjoner som sørger for flyt og utveksling av data mellom systemer, samarbeidspartnere og sluttkunder. Vi utvikler maskinlæringsmodeller som effektiviserer og forenkler kundens hverdag.</p>
  </div>
</section>

<svg class="focus-diagram" viewBox="0 0 674 287" preserveAspectRatio="none" role="img" aria-label="Diagram of TLV focus areas">
  <defs>
    <linearGradient id="diagramBg" x1="0" x2="1" y1="0" y2="0">
      <stop offset="0" stop-color="#6e8db4"/><stop offset=".55" stop-color="#4a6284"/><stop offset="1" stop-color="#2a2b2f"/>
    </linearGradient>
    <linearGradient id="boxFill" x1="0" x2="1">
      <stop offset="0" stop-color="#f59846"/><stop offset=".75" stop-color="#f08a52"/><stop offset="1" stop-color="#ec5a5a"/>
    </linearGradient>
  </defs>
  <rect width="674" height="287" fill="url(#diagramBg)"/>
  <g font-family="Montserrat, sans-serif" fill="#fff">
    <text x="64" y="52" font-size="9">Tallvik Focus</text>
    <text x="373" y="52" font-size="9">Tallvik Consulting</text>
    <rect x="60" y="58" width="250" height="95" fill="url(#boxFill)"/>
    <rect x="369" y="58" width="251" height="95" fill="url(#boxFill)"/>
    <g font-size="8.2" font-weight="500">
      <text x="65" y="89">VI SKAL VÆRE EN LEDENDE LEVERANDØR AV BI</text>
      <text x="65" y="102">KONSULENTTJENESTER OG LØSNINGER FOR</text>
      <text x="65" y="116">FORRETNINGSSTØTTE OG VIRKSOMHETSTYRING,</text>
      <text x="65" y="129">HOVEDSAKELIG PÅ CLOUDVALE PLATTFORMEN</text>
      <text x="374" y="89">VI SKAL VÆRE LANDETS LEDENDE LEVERANDØR OG</text>
      <text x="374" y="102">KOMPETANSEHUS PÅ TALLVIK PROGRAMVARE</text>
      <text x="374" y="115">OG DIGITALE LØSNINGER FOR</text>
      <text x="374" y="129">VIRKSOMHETSSTYRING</text>
    </g>
  </g>
  <g stroke="#cfd6e0" stroke-width="1" fill="none">
    <path d="M185 153 V190 M494 153 V190 M64 190 H612 M64 190 V225 M278 190 V225 M390 190 V225 M500 190 V225 M612 190 V225"/>
  </g>
  <g fill="#fff">
    <path d="M52 248 a8 8 0 0 1 8-10 a10 10 0 0 1 18 3 a6 6 0 0 1 0 11 h-24 a5 5 0 0 1 -2-4 Z"/>
    <circle cx="92" cy="232" r="1.5"/><circle cx="92" cy="244" r="1.5"/><circle cx="92" cy="256" r="1.5"/><circle cx="92" cy="268" r="1.5"/>
    <rect x="268" y="235" width="3" height="12"/><rect x="273" y="230" width="3" height="17"/><rect x="278" y="238" width="3" height="9"/><rect x="283" y="228" width="3" height="19"/>
    <rect x="386" y="229" width="8" height="6"/><rect x="376" y="243" width="7" height="6"/><rect x="386" y="243" width="7" height="6"/><rect x="396" y="243" width="7" height="6"/>
    <rect x="493" y="230" width="5" height="17" rx="2"/><rect x="502" y="230" width="5" height="17" rx="2"/>
  </g>
  <g stroke="#fff" stroke-width="1.3" fill="none">
    <path d="M278 227 V252 H292"/>
    <path d="M390 235 V239 M379 243 V239 H400 V243"/>
    <rect x="602" y="231" width="20" height="15"/>
    <path d="M609 236 l-3 3 l3 3 M615 236 l3 3 l-3 3 M613 235 l-2 8"/>
  </g>
  <g font-family="Montserrat, sans-serif" font-weight="700" font-size="8.6" fill="#fff">
    <text x="103" y="236">DATAVAREHUS</text>
    <text x="103" y="248">DATAVISUALISERING</text>
    <text x="103" y="260">INTEGRASJONER</text>
    <text x="103" y="272">MASKINLÆRING</text>
    <text x="276" y="279" text-anchor="middle">BUSINESS INTELLIGENCE</text>
    <text x="390" y="279" text-anchor="middle">CONSOLIDATION</text>
    <text x="494" y="279" text-anchor="middle">PLANNING</text>
    <text x="612" y="279" text-anchor="middle">CUSTOME SOLUTIONS</text>
  </g>
</svg>

<section class="contact" id="contact">
  <h2 class="section-title">Contact Us</h2>
  <span class="section-rule"></span>
  <form class="contact-form" action="#">
    <div class="field f-first">First name *</div>
    <div class="field f-last">Last name *</div>
    <div class="field f-mail">Your mail *</div>
    <div class="field f-phone">Phone number *</div>
    <div class="field f-message">Message...</div>
    <div class="btn-send">SEND MESSAGE</div>
  </form>
</section>

</body>
</html>
```